Business cards for Paperleaf Sprites

Please note that the color of the logo has been changed from green to teal blue. Sorry for the changing!

Anything will go but want to have some funky side.

I would like the front of the business card is the logo and business information and the back side is the Adult Coloring, so that would attract the customer to do the coloring on the other side. Have more interactive side. (pictures for references only can see it below). Fairies on the back of the card for coloring and whatever you want to adds on to color, like flowers, nature etc......

Scrapbooking is not just paper, it also involves watercolor, mixed media, art, all the fun stuff.

Another keypoint I would like to stress on is the back of the business card should be Adult Coloring and make sure you are not google and use the search engine to copy and paste because of the copyright issue.

As a designer, I am sure you all can create beautiful artwork.

Please submit your creativities!

Want the business card is out of the ordinary and customers would like to keep that as a keepsake rather than treat like a regular business card and trash it. Fonts cannot be too small, consider some of the customers have to wear bi-focal eyeglasses.

Thanks a lot!

Target Market(s)

Scrapbooking, Card making, papercraft, stampin‘ , gifts items , etc.

Industry/Entity Type

Retail

Contact Information for Business Card

Color Scheme, please match with the Logo. Watercolor effect is nice!
Thanks!

Font styles to use
Serif

Requirements
Must have
• I would like Elegant and playful.
• Thanks!
Nice to have
• Watercolor effect or check out the Adult Coloring Book, I am thinking we can use a double-sided business card, one side for the information and the other side for people can do the coloring. I have attached 2 pictures for reference.
Should not have
• No black color on the background please!

```html
<!DOCTYPE html>
<html lang="en">
<head>
<meta charset="utf-8">
<title>Paperleaf Sprites – Business Card</title>
<link rel="stylesheet" href="https://fonts.googleapis.com/css2?family=Lobster&family=Josefin+Sans:wght@300;400&family=Nunito:wght@400;800&display=swap">
<style>
  :root {
    --page-bg: #e9e6e2;
    --card-white: #ffffff;
    --teal: #2f7f93;
    --teal-soft: #bfe6dc;
    --mint-wash: #9fdcca;
    --berry-red: #b0232e;
    --ink: #2b2b2b;
    --petal: #ef7f86;
    --leaf: #7cbf96;
  }
  * { box-sizing: border-box; margin: 0; padding: 0; }
  html, body { width: 1200px; height: 1200px; overflow: hidden; }
  body { background: var(--page-bg); position: relative; }

  .card {
    position: absolute;
    left: 280px;
    width: 638px;
    height: 403px;
    background: var(--card-white);
    overflow: hidden;
    box-shadow: 0 4px 14px rgba(0,0,0,0.12);
  }
  .card--front { top: 159px; }
  .card--back { top: 638px; }

  .card__frame {
    position: absolute;
    inset: 18px 17px;
    border: 1px solid var(--teal-soft);
    pointer-events: none;
  }
  .card--back .card__frame { border-color: var(--teal); inset: 19px 17px 19px 18px; }

  /* front */
  .watercolor-splash {
    position: absolute;
    left: 140px; top: 10px;
    width: 340px; height: 390px;
    border-radius: 46% 54% 40% 60% / 45% 40% 60% 55%;
    background: radial-gradient(ellipse at 50% 50%, rgba(159,220,202,0.75) 0%, rgba(159,220,202,0.45) 55%, rgba(159,220,202,0) 75%);
  }
  .brand-name {
    position: absolute;
    left: 0; right: 0; top: 174px;
    text-align: center;
    font-family: "Nunito", sans-serif;
    font-weight: 800;
    font-size: 50px;
    letter-spacing: 1px;
    color: var(--teal);
  }

  /* back */
  .wash { position: absolute; }
  .wash--right {
    right: -40px; top: -20px; width: 260px; height: 230px;
    border-radius: 40% 60% 55% 45% / 50% 40% 60% 50%;
    background: radial-gradient(ellipse at 60% 35%, rgba(159,220,202,0.7) 0%, rgba(159,220,202,0.35) 55%, rgba(159,220,202,0) 78%);
  }
  .wash--left {
    left: -60px; top: 150px; width: 200px; height: 280px;
    border-radius: 50% 50% 45% 55% / 40% 55% 45% 60%;
    background: radial-gradient(ellipse at 40% 55%, rgba(159,220,202,0.65) 0%, rgba(159,220,202,0.3) 55%, rgba(159,220,202,0) 78%);
  }
  .floral { position: absolute; border-radius: 50%; }
  .floral--left {
    left: 0; top: 40px; width: 130px; height: 190px;
    border-radius: 40% 60% 50% 50%;
    background: radial-gradient(ellipse at 55% 45%, rgba(239,127,134,0.35) 0%, rgba(124,191,150,0.3) 45%, rgba(124,191,150,0) 72%);
  }
  .floral--bottom-right {
    right: 0; bottom: 0; width: 100px; height: 110px;
    background: radial-gradient(ellipse at 70% 45%, rgba(239,127,134,0.45) 0%, rgba(124,191,150,0.35) 50%, rgba(124,191,150,0) 74%);
  }
  .floral--top-right {
    right: 30px; top: 30px; width: 140px; height: 150px;
    background: radial-gradient(ellipse at 50% 50%, rgba(170,170,190,0.25) 0%, rgba(200,180,150,0.2) 45%, rgba(200,180,150,0) 72%);
  }

  .contact {
    position: absolute;
    left: 0; right: 0;
    text-align: center;
    color: var(--ink);
  }
  .contact__name {
    top: 72px;
    font-family: "Lobster", cursive;
    font-size: 42px;
    color: var(--berry-red);
  }
  .contact__email {
    top: 133px;
    font-family: "Nunito", sans-serif;
    font-size: 15px;
    letter-spacing: 0.5px;
  }
  .contact__divider {
    position: absolute;
    left: 18px; right: 18px; top: 181px;
    border-top: 2px dotted #d2d2d2;
  }
  .contact__address {
    top: 203px;
    font-family: "Josefin Sans", sans-serif;
    font-weight: 300;
    font-size: 18px;
    line-height: 24px;
    letter-spacing: 1px;
  }
  .contact__phone {
    top: 290px;
    font-family: "Josefin Sans", sans-serif;
    font-weight: 300;
    font-size: 26px;
    color: var(--teal);
    display: flex; justify-content: center; align-items: center; gap: 6px;
  }
  .contact__phone svg { width: 12px; height: 18px; }
  .contact__web {
    top: 334px;
    font-family: "Nunito", sans-serif;
    font-size: 18px;
    letter-spacing: 0.8px;
  }
</style>
</head>
<body>
  <section class="card card--front">
    <div class="watercolor-splash" role="img" aria-label="Soft mint watercolour splash behind the name"></div>
    <div class="card__frame"></div>
    <div class="brand-name">Paperleaf Sprites</div>
  </section>

  <section class="card card--back">
    <div class="wash wash--right" role="img" aria-label="Mint watercolour wash"></div>
    <div class="wash wash--left" role="img" aria-label="Mint watercolour wash"></div>
    <div class="floral floral--left" role="img" aria-label="Watercolour berry branch and pink flower"></div>
    <div class="floral floral--top-right" role="img" aria-label="Watercolour falling leaves"></div>
    <div class="floral floral--bottom-right" role="img" aria-label="Watercolour pink flower with green leaves"></div>
    <div class="card__frame"></div>

    <div class="contact contact__name">Rosalind Varga</div>
    <div class="contact contact__email">hello@paperleafsprites.com</div>
    <div class="contact__divider"></div>
    <div class="contact contact__address">
      Unit 4, 1820-37 Avenue, PO Box 2290<br>
      Maplebrook, Alberta<br>
      Canada T0X 2K4
    </div>
    <div class="contact contact__phone">
      <svg viewBox="0 0 12 18" aria-hidden="true"><path d="M9 1 C4 1 2 5 2 9 C2 13 4 17 9 17 L10 13 L7 12.5 C6 11 6 7 7 5.5 L10 5 Z" fill="#b0232e"/></svg>
      <span>(555) 418-2736</span>
    </div>
    <div class="contact contact__web">www.paperleafsprites.com</div>
  </section>
</body>
</html>
```